Uprising SaaS company needs an attractive business card design

We're an uprising SaaS company who's attempting to attack the rigid car (insurance) claims management market in Europe.
We want to our mighty base order management system, listen to our clients to connect the smart ideas to build something even mightier.
We primarily focus on helping our customers manage their customers' claims/orders and get them resolved as smoothly as possible.
We'd like the business card design to express technical innovation and the fact that we connect smart ideas, as our company slogan indicates.
Contact Information for Business Card
Name, position, website, email, mobile, business address
Font styles to use
Colors
Designer to choose colors to be used in the design.
Look and feel
Each slider illustrates characteristics of the customer's brand and the style your logo design should communicate.

```html
<!DOCTYPE html>
<html lang="en">
<head>
<meta charset="utf-8">
<title>nodevia business card</title>
<link rel="stylesheet" href="https://fonts.googleapis.com/css2?family=Questrial&family=Arimo:wght@400;700&display=swap">
<style>
  :root {
    --backdrop: #c4c4c4;
    --card-white: #ffffff;
    --brand-blue: #84cfe4;
    --accent-blue: #6cc3df;
    --ink: #1e1e1e;
    --ink-grey: #7a7a7a;
    --rule: #9a9a9a;
  }
  * { box-sizing: border-box; margin: 0; padding: 0; }
  html, body { width: 1200px; height: 800px; overflow: hidden; }
  body {
    background: var(--backdrop);
    display: flex;
    align-items: center;
    justify-content: center;
    gap: 40px;
    font-family: "Arimo", Arial, sans-serif;
  }
  .card {
    position: relative;
    width: 520px;
    height: 297px;
    box-shadow: 0 10px 24px rgba(0,0,0,0.25);
  }
  .card-front { background: var(--card-white); border-bottom: 3px solid var(--accent-blue); }
  .wordmark {
    position: absolute;
    left: 40px;
    top: 160px;
    font-family: "Questrial", sans-serif;
    font-size: 52px;
    letter-spacing: 1px;
    color: var(--ink-grey);
  }
  .divider {
    position: absolute;
    left: 268px;
    top: 46px;
    width: 1px;
    height: 206px;
    background: var(--rule);
  }
  .contact {
    position: absolute;
    left: 286px;
    top: 58px;
    color: var(--ink);
    font-size: 12.5px;
    line-height: 1.35;
  }
  .person-name {
    font-family: "Questrial", sans-serif;
    font-size: 22px;
    color: var(--ink-grey);
    letter-spacing: 0.5px;
    line-height: 1.1;
  }
  .person-name .surname { color: var(--accent-blue); }
  .person-role { font-size: 13px; margin-bottom: 12px; }
  .contact-line { display: flex; align-items: center; gap: 6px; }
  .contact-line svg { width: 12px; height: 12px; flex: none; }
  .contact-line .highlight { color: var(--accent-blue); }
  .address { margin-top: 12px; padding-left: 18px; }
  .card-back {
    background: var(--brand-blue);
    display: flex;
    align-items: center;
    justify-content: center;
  }
  .card-back .wordmark-back {
    font-family: "Questrial", sans-serif;
    font-size: 40px;
    letter-spacing: 1px;
    color: var(--card-white);
  }
</style>
</head>
<body>
  <section class="card card-front">
    <div class="wordmark">nodevia</div>
    <div class="divider"></div>
    <div class="contact">
      <div class="person-name">Daniel <span class="surname">Harper</span></div>
      <div class="person-role">Managing Director</div>
      <div class="contact-line">
        <svg viewBox="0 0 12 12" aria-hidden="true"><path d="M2.5 1 L4.5 1 L5.3 3.3 L4 4.3 Q5 6.8 7.7 8 L8.7 6.7 L11 7.5 L11 9.5 Q10.5 11 9 11 Q1 10 1 3 Q1 1.5 2.5 1 Z" fill="var(--accent-blue)"/></svg>
        <span>044-987 654 321</span>
      </div>
      <div class="contact-line">
        <svg viewBox="0 0 12 12" aria-hidden="true"><rect x="0.5" y="2.5" width="11" height="7.5" fill="var(--accent-blue)"/><path d="M0.8 2.8 L6 7 L11.2 2.8" stroke="#fff" stroke-width="1" fill="none"/></svg>
        <span>hello@mailsample.com</span>
      </div>
      <div class="contact-line">
        <svg viewBox="0 0 12 12" aria-hidden="true"><circle cx="6" cy="6" r="5.2" fill="var(--accent-blue)"/><path d="M0.8 6 H11.2 M6 0.8 V11.2 M6 0.8 Q2.5 6 6 11.2 M6 0.8 Q9.5 6 6 11.2" stroke="#fff" stroke-width="0.7" fill="none"/></svg>
        <span>www.<span class="highlight">sitesample</span>.com</span>
      </div>
      <div class="address">
        88, Harbour Lane Street East<br>
        20817, Northland
      </div>
    </div>
  </section>

  <section class="card card-back" role="img" aria-label="Blue card back with a faint repeated brand pattern behind the centred company name">
    <div class="wordmark-back">nodevia</div>
  </section>
</body>
</html>
```